2-sided DIN A5 flyer for Real Estate company

Please read carefully: - Flyers should be in A5, 2-sided - Design should be eye-catching but still looking serious and trustful, modern, fresh, clean - The flyer will be sent to households. On the flyer it says that people can earn money. So the flyer should be animate people to contact me and share information with me. - The text you can use is written in «text». Please use different font sizes. Fontsize indication is written in front of «text». I would like to be able to do this in the future. I would like to be able to do this. * Update afterfirst designs I received * If you use pictures, keep in mind the reader of the flyer will not sell me a house, he will sell me a contact. So it is worth the money to pay for the money. If you use money, please use swiss currency money picture! But overall the text should be in the focus, especially on front side! The logo of my company is not too important! Front side: - Logo - Eye-catching design using the color theme of logo, not just one background color, maybe different blues - The text should be in the focus and as big as possible. Play with different sizes, bold / unbold, capital letters, etc. The goal should be that the text is the first thing that the reader see. - Dont use too many pictures. If so, you can use a graphical for tip (ie light bubble) in front of a real estate, then an equal sign and then a graphical for money or incentive. Cause thats what they get. - Big-font: «Your tip is us up to CHF 3 '- Big-font:« Big-font: 500.- worth! »- Phone icon, medium-font:« 044 618 53 90 »- Mail icon, medium-font:« ch@valdorf-immo.ch »- Website icon, medium-font:« www.valdorf- Immo.ch »Back side: Big-font:« Your tip is worth MONEY! "Medium-font:" You know a potential real estate salesman in your family, friends, acquaintances, club or professional world? Whether immediate or in the near future your tip can pay off for you. After a successful placement we will give you a tip-and-shoot commission of up to CHF 3'500 .-- »Medium-font. «And as simple as this works: 1. You contact us and give us the willing owner 2. We contact the owner and conclude a brokerage from 3. We start the sales process and inform you about the progress 4. After you have successfully completed your sales contract, you will receive your donor commission! »Medium-font. «Example: Thanks to your tip we can sell a property to 1.5 million. Your donor commission is CHF 3'000 .-- (0.2% of CHF 1'500'000.-) »Medium-font. "Valdorf Immobilien Treuhand AG Lindmattweg 14 8053 Zürich" - Phone icon, medium-font: «044 618 53 90» - Mail icon, medium-font: «ch@valdorf-immo.ch» - Website icon, medium-font: « Www.valdorf-immo.ch "Very-small-font at bottom of flyer" * The Tippgeberprovision is paid out after the public noti fi cation of the purchase contract as well as after receipt of the mediation commission. The donor commission is 0.2% of the selling price, but the maximum is CHF 3'500 .--. In the event of non-compliance with our mediation commission, payment of the donor commission can not be made. The donor guaranty is only paid once per object and only applies to objects that are not known to us at the time of your contact. We reserve the right to refuse, at our own discretion, any objects, owners or operators. The legal process is excluded. »

Target Market(s)

Every household

Industry/Entity Type

Real Estate

Font styles to use
Serif
Sans Serif

Colors
0255a3
3277b5
33a6d7
85cae6
cfdfed
0692cd

Requirements
Must have
• See project description

```html
<!DOCTYPE html>
<html lang="de">
<head>
<meta charset="utf-8">
<title>Valdorf Immobilien – Tippgeber Flyer</title>
<link href="https://fonts.googleapis.com/css2?family=Open+Sans:ital,wght@0,400;0,600;0,700;0,800;1,400;1,600&display=swap" rel="stylesheet">
<style>
:root{
  --navy:#112f55;
  --blue:#1f62ad;
  --blue-mid:#3277b5;
  --sky:#33a6d7;
  --ice:#cfdfed;
  --paper:#ffffff;
  --ink:#1d2a3a;
  --backdrop:#e6ebf0;
}
*{box-sizing:border-box;margin:0;padding:0}
html,body{width:1200px;height:800px;overflow:hidden;background:var(--backdrop);font-family:"Open Sans",Arial,sans-serif;color:var(--ink)}
.canvas{position:relative;width:1200px;height:800px}
.page{position:absolute;top:18px;width:538px;height:764px;background:var(--paper);overflow:hidden;box-shadow:0 6px 18px rgba(0,0,0,.18)}
.page--front{left:46px}
.page--back{left:616px}
.abs{position:absolute}

/* front */
.brand{left:30px;top:46px;display:flex;align-items:center;gap:9px}
.brand__mark{width:16px;height:16px;background:var(--blue)}
.brand__name{font-weight:700;font-size:20px;color:var(--navy);letter-spacing:1px;white-space:nowrap}
.address{right:16px;top:30px;font-size:11px;line-height:16px;color:var(--ink);white-space:nowrap}
.address__firm{color:var(--blue);display:flex;align-items:center;gap:4px}
.address__lines{padding-left:17px}
.top-band{left:250px;top:98px;width:288px;height:16px;background:var(--blue);clip-path:polygon(4% 0,100% 0,100% 100%,0 100%)}
.photo{left:0;top:112px;width:538px;height:306px;background:linear-gradient(120deg,#8fa7a0 0%,#6d8db0 35%,#a9b8c8 55%,#5d84b4 75%,#8aa3b4 100%)}
.photo-band{left:0;top:418px;width:300px;height:12px;background:var(--blue);clip-path:polygon(0 0,100% 0,96% 100%,0 100%)}
.headline{left:10px;top:440px;background:var(--navy);color:#fff;font-weight:700;font-size:33px;padding:4px 36px 6px 14px;white-space:nowrap}
.subline{left:8px;top:494px;background:var(--blue-mid);color:#fff;font-style:italic;font-size:24px;padding:4px 10px 6px 14px;white-space:nowrap}
.tip-box{left:14px;top:574px;width:198px;height:146px;background:var(--navy)}
.tip-box__head{background:var(--blue);color:#fff;font-weight:700;font-size:34px;padding:4px 0 4px 28px;height:56px}
.tip-box__mid{color:#fff;font-weight:700;font-size:19px;padding:8px 0 0 30px}
.tip-box__value{position:absolute;left:14px;top:102px;background:#fff;color:var(--blue);font-weight:800;font-size:19px;padding:2px 4px;white-space:nowrap}
.tip-box__value b{color:var(--navy)}
.pitch{left:228px;top:620px}
.pitch__title{font-weight:700;font-size:25px;color:var(--navy)}
.pitch__italic{font-style:italic;font-size:12.5px;color:var(--ink)}
.pitch__line{font-size:15px;color:var(--ink);margin-top:4px}
.footer{left:0;bottom:0;width:538px;height:44px;background:var(--blue);color:#fff;font-weight:700;font-size:12px;display:flex;align-items:center;justify-content:center;gap:12px}
.footer__item{display:flex;align-items:center;gap:6px}
.footer__sep{opacity:.8}
.icon{width:13px;height:13px;fill:#fff;flex:none}

/* back */
.bh{left:20px;background:var(--navy);color:#fff;font-weight:700;white-space:nowrap;padding:0 8px}
.bh--1{top:36px;font-size:23px}
.bh--2{top:72px;font-size:22px;background:var(--blue)}
.bh--3{top:108px;font-size:28px}
.figure{left:360px;top:20px;width:150px;height:150px;border-radius:50% 50% 40% 40%;background:radial-gradient(circle at 60% 45%,#33a6d7 0%,#85cae6 45%,#ffffff 75%)}
.intro{left:20px;top:174px;width:502px;background:var(--blue);color:#fff;font-weight:600;font-size:14.2px;line-height:22px;padding:16px 10px 10px 8px}
.steps{left:16px;top:362px;width:248px}
.steps__head{background:var(--blue);color:#fff;font-weight:700;font-size:30px;padding:6px 10px 2px 10px}
.steps__sub{background:var(--navy);color:#fff;font-weight:700;font-size:16px;padding:4px 10px 6px}
.steps__list{list-style:none;margin-top:10px;font-size:11.5px;line-height:15px}
.steps__list li{display:flex;gap:6px;margin-bottom:9px}
.steps__list span{color:var(--blue-mid)}
.example{left:276px;top:356px;width:246px;background:var(--navy);color:#fff;padding-bottom:14px}
.example__head{background:var(--blue);font-weight:700;font-size:30px;padding:8px 12px;height:60px}
.example__body{padding:6px 12px 0}
.example__l1{font-weight:600;font-size:19px}
.example__l2{font-size:15.5px}
.example__l3{font-weight:700;font-size:21px}
.example__l4{font-size:15.5px;margin-top:6px;line-height:21px}
.example__value{background:#fff;color:var(--navy);font-weight:800;font-size:27px;padding:0 6px;margin:8px 0 0;width:212px}
.example__value span{color:var(--blue);font-weight:600}
.fine{left:20px;top:612px;width:502px;font-size:7.6px;line-height:10.5px;color:var(--ink)}
.back-footer{left:0;bottom:38px;width:538px;height:38px;background:var(--blue);color:#fff;font-weight:700;font-size:12px;display:flex;align-items:center;justify-content:center;gap:12px}
.back-address{left:0;bottom:0;width:538px;height:38px;background:var(--navy);color:#fff;font-size:11.5px;display:flex;align-items:center;justify-content:center;gap:6px}
</style>
</head>
<body>
<main class="canvas">

  <section class="page page--front" aria-label="Vorderseite">
    <div class="abs brand"><span class="brand__mark"></span><span class="brand__name">VALDORF IMMOBILIEN</span></div>
    <div class="abs address">
      <div class="address__firm"><svg class="icon" style="fill:var(--blue)" viewBox="0 0 24 24"><path d="M12 2a7 7 0 0 0-7 7c0 5 7 13 7 13s7-8 7-13a7 7 0 0 0-7-7zm0 9.5A2.5 2.5 0 1 1 12 6.5a2.5 2.5 0 0 1 0 5z"/></svg>Valdorf Immobilien + Treuhand AG</div>
      <div class="address__lines">Lindmattweg 14<br>8053 Zürich"</div>
    </div>
    <div class="abs top-band"></div>
    <div class="abs photo" role="img" aria-label="Foto von Schweizer Banknoten in Grün, Blau und Rot"></div>
    <div class="abs photo-band"></div>
    <h1 class="abs headline">Ihr TIPP ist GELD wert!</h1>
    <p class="abs subline">Verraten Sie ihn uns noch heute!</p>
    <div class="abs tip-box">
      <div class="tip-box__head">Ihr Tipp</div>
      <div class="tip-box__mid">ist uns bis zu</div>
      <div class="tip-box__value"><b>CHF 3'500.</b>- wert!</div>
    </div>
    <div class="abs pitch">
      <div class="pitch__title">Sie kennen jemanden</div>
      <div class="pitch__italic">der sein Haus oder seine Wohnung verkaufen will?</div>
      <div class="pitch__line">Ihr Tipp ist uns bis zu CHF 3'500.- wert!"</div>
    </div>
    <footer class="abs footer">
      <span class="footer__item"><svg class="icon" viewBox="0 0 24 24"><path d="M3 9c0-3 4-5 9-5s9 2 9 5v2h-5V9H8v2H3zm3 3h12l2 8H4z"/></svg>044 618 53 90</span><span class="footer__sep">|</span>
      <span class="footer__item"><svg class="icon" viewBox="0 0 24 24"><path d="M2 5h20v14H2zm2 2v.5l8 5 8-5V7z"/></svg>ch@valdorf-immo.ch</span><span class="footer__sep">|</span>
      <span class="footer__item"><svg class="icon" viewBox="0 0 24 24"><circle cx="12" cy="12" r="9" fill="none" stroke="#fff" stroke-width="2"/><path d="M3 12h18M12 3c3 3 3 15 0 18M12 3c-3 3-3 15 0 18" fill="none" stroke="#fff" stroke-width="1.5"/></svg>www.valdorf-immo.ch</span>
    </footer>
  </section>

  <section class="page page--back" aria-label="Rückseite">
    <h2 class="abs bh bh--1">Ihr TIPP ist GELD wert!</h2>
    <p class="abs bh bh--2">Verraten Sie ihn uns</p>
    <p class="abs bh bh--3">noch heute!</p>
    <div class="abs figure" role="img" aria-label="3D-Illustration einer Figur neben einem grossen blauen Fragezeichen"></div>
    <p class="abs intro">Sie kennen in der Familie, im Freundeskreis, im Bekanntenkreis, im Verein oder aus der Berufswelt einen potentiellen Immobilienverkäufer? Ob sofort oder in naher Zukunft kann sich Ihr Tipp für Sie auszahlen. Tippgeber erhalten von uns nach einer erfolgreichen Vermittlung eine Tippgeberprovision von bis zu CHF 3'500</p>
    <div class="abs steps">
      <div class="steps__head">Und so einfach</div>
      <div class="steps__sub">funktionierts:</div>
      <ol class="steps__list">
        <li><span>1.</span>Sie kontaktieren uns und geben uns den verkaufswilligen Eigentümer an</li>
        <li><span>2.</span>Wir kontaktieren den Eigentümer und schliessen einen Maklervertrag ab</li>
        <li><span>3.</span>Wir starten den Verkaufsprozess und informieren Sie über die Fortschritte</li>
        <li><span>4.</span>Nach erfolgreichem Verkaufsabschluss erhalten Sie Ihre Tippgeberprovision!</li>
      </ol>
    </div>
    <div class="abs example">
      <div class="example__head">Beispiel:</div>
      <div class="example__body">
        <div class="example__l1">Dank Ihrem Tipp</div>
        <div class="example__l2">können wir eine Immobilie zu</div>
        <div class="example__l3">1.5 Mio verkaufen</div>
        <div class="example__l4">Ihre Tippgeberprovision<br>beträgt in dem Fall</div>
        <div class="example__value"><span>CHF</span> 3'000.</div>
      </div>
    </div>
    <p class="abs fine">Die Tippgeberprovision wird nach der öffentlichen Beurkundung des Kaufvertrags sowie nach Erhalt der Vermittlungsprovision ausbezahlt. Die Tippgeberprovision beträgt 0.2% des erzielten Verkaufspreises, im Maximum jedoch CHF 3'500.--. Bei Nichterhalt unserer Vermittlungsprovision kann auch keine Auszahlung der Tippgeberprovision erfolgen. Die Tippgeberprovision wird pro Objekt nur einmalig ausbezahlt und gilt nur für Objekte, die uns zum Zeitpunkt Ihrer Kontaktaufnahme noch nicht bekannt sind. Wir behalten uns das Recht vor nach eigenem Ermessen Objekte, Eigentümer oder Tippgeber abzulehnen. Der Rechtsweg ist ausgeschlossen</p>
    <div class="abs back-footer">
      <span class="footer__item"><svg class="icon" viewBox="0 0 24 24"><path d="M3 9c0-3 4-5 9-5s9 2 9 5v2h-5V9H8v2H3zm3 3h12l2 8H4z"/></svg>044 618 53 90</span><span class="footer__sep">|</span>
      <span class="footer__item"><svg class="icon" viewBox="0 0 24 24"><path d="M2 5h20v14H2zm2 2v.5l8 5 8-5V7z"/></svg>ch@valdorf-immo.ch</span><span class="footer__sep">|</span>
      <span class="footer__item"><svg class="icon" viewBox="0 0 24 24"><circle cx="12" cy="12" r="9" fill="none" stroke="#fff" stroke-width="2"/><path d="M3 12h18M12 3c3 3 3 15 0 18M12 3c-3 3-3 15 0 18" fill="none" stroke="#fff" stroke-width="1.5"/></svg>www.valdorf-immo.ch</span>
    </div>
    <div class="abs back-address">
      <svg class="icon" viewBox="0 0 24 24"><path d="M12 2a7 7 0 0 0-7 7c0 5 7 13 7 13s7-8 7-13a7 7 0 0 0-7-7zm0 9.5A2.5 2.5 0 1 1 12 6.5a2.5 2.5 0 0 1 0 5z"/></svg>
      Valdorf Immobilien + Treuhand AG Lindmattweg 14 8053 Zürich
    </div>
  </section>

</main>
</body>
</html>
```